Velmarind

We need a website redesign for a Wordpress-based template. We have WP and Elementor and are looking for a template to modernise the existing website at http://www.velmarind.co.uk. we can handle the relocation of the content but want a new fresh look. As an example, http://brovy.io looks nice.

```html
<!DOCTYPE html>
<html lang="en">
<head>
<meta charset="utf-8">
<title>Velmarind – Drug Repurposing</title>
<link href="https://fonts.googleapis.com/css2?family=Roboto:wght@400;500;700&family=Roboto+Slab:wght@400;700&display=swap" rel="stylesheet">
<style>
:root{
  --green:#3d9a1b;
  --yellow:#f8f306;
  --ink:#2b2b2b;
  --grey:#6f6f6f;
  --light:#f3f3f3;
  --rule:#e2e2e2;
  --logo:#2f4f4f;
}
*{box-sizing:border-box;margin:0;padding:0}
html,body{width:898px;height:1200px;overflow:hidden;background:#fff}
body{font-family:'Roboto',sans-serif;color:var(--ink);position:relative}
.site-header{height:85px;position:relative}
.brand{position:absolute;left:65px;top:28px;display:flex;align-items:center;gap:8px;font-size:22px;font-weight:500;color:var(--logo)}
.brand-mark{width:16px;height:16px;border-radius:50%;background:var(--green)}
.main-nav{position:absolute;right:66px;top:34px;display:flex;gap:21px;font-size:10px;text-transform:uppercase;color:#333}
.main-nav .active{font-weight:500;color:#111}
.caret{font-size:7px;margin-left:3px}
.active-dot{position:absolute;left:410px;top:55px;width:9px;height:9px;border-radius:50%;background:var(--green)}
.hero{position:absolute;top:85px;left:0;width:898px;height:358px;background:radial-gradient(ellipse at 40% 45%,#1a7a8e 0%,#0c3f5c 45%,#040f22 85%);display:flex;align-items:center;justify-content:center}
.hero h1{font-family:'Roboto Slab',serif;font-weight:700;color:#fff;font-size:25px;line-height:36px;text-align:center;text-transform:uppercase;margin-top:-17px;text-shadow:0 2px 4px rgba(0,0,0,.5)}
.hero-dots{position:absolute;bottom:27px;left:50%;transform:translateX(-50%);display:flex;gap:5px}
.hero-dots span{width:8px;height:8px;border:1.5px solid #fff;border-radius:50%}
.hero-dots span.on{background:#fff}
.mission{position:absolute;top:443px;left:0;width:898px;height:238px;background:var(--light);text-align:center}
.section-title{font-family:'Roboto Slab',serif;font-weight:400;color:var(--ink)}
.mission .section-title{font-size:17px;margin-top:46px;display:flex;justify-content:center;align-items:center;gap:12px}
.title-dot{width:11px;height:11px;border-radius:50%;background:var(--green)}
.mission p{width:560px;margin:14px auto 0;font-size:9.8px;line-height:16px;color:var(--grey)}
.split-btn{display:inline-flex;border-radius:12px;overflow:hidden;font-size:8.5px;font-weight:700;text-transform:uppercase;height:23px}
.split-btn span{display:flex;align-items:center;padding:0 12px}
.split-btn .a{background:var(--yellow);color:#333}
.split-btn .b{background:var(--green);color:#fff;margin-left:2px}
.mission .split-btn{margin-top:25px}
.book{position:absolute;top:681px;left:0;width:898px;height:377px}
.book-col{position:absolute;top:58px;left:100px;width:238px;text-align:center}
.book-col .section-title{font-size:13.5px;margin-left:-10px}
.book-cover{width:176px;height:106px;margin:20px auto 0;background:linear-gradient(90deg,#d7dde6,#3b78c9 50%,#cfd1d3);border-radius:2px}
.year{font-size:10.5px;margin-top:25px;color:#333}
.author{font-size:9.5px;color:#555;margin-top:2px}
.stars{margin-top:13px;display:flex;justify-content:center}
.book-col .split-btn{margin-top:18px}
.divider{position:absolute;left:414px;top:59px;width:1px;height:258px;background:var(--rule)}
.reviews{position:absolute;top:52px;left:490px;width:292px;text-align:center}
.reviews .section-title{font-size:13.5px}
.review{font-size:9.5px;line-height:15.5px;color:var(--grey);margin-top:13px}
.review cite{display:block;font-style:normal;color:var(--green);margin-top:13px}
.review-rule{width:196px;height:1px;background:var(--rule);margin:16px auto 0}
.reviews .split-btn{margin-top:25px}
.newsletter{position:absolute;top:1058px;left:0;width:898px;height:77px;background:linear-gradient(180deg,var(--green) 0%,#5aa52b 55%,#b7c9a9 100%);display:flex;align-items:center}
.newsletter h2{font-size:15px;font-weight:500;color:#fff;text-transform:uppercase;margin-left:152px}
.email-field{margin-left:32px;width:275px;height:32px;border:1.5px solid #fff;border-radius:16px;color:#fff;font-size:9.5px;display:flex;align-items:center;padding-left:15px}
.subscribe{margin-left:8px;width:79px;height:32px;border-radius:14px;background:var(--yellow);font-size:10px;font-weight:700;display:flex;align-items:center;justify-content:center;text-transform:uppercase;color:#222}
.site-footer{position:absolute;top:1135px;left:0;width:898px;height:65px}
.copyright{position:absolute;left:65px;top:27px;font-size:9px;color:#555}
.social{position:absolute;right:65px;top:27px;display:flex;gap:6px}
.social span{width:20px;height:20px;border:1.3px solid var(--green);border-radius:50%}
</style>
</head>
<body>
<header class="site-header">
  <div class="brand">Velmarind <span class="brand-mark"></span></div>
  <nav class="main-nav">
    <span class="active">Home</span>
    <span>About<span class="caret">&#9662;</span></span>
    <span>Therapeutic Switching<span class="caret">&#9662;</span></span>
    <span>Services<span class="caret">&#9662;</span></span>
    <span>Blog</span>
    <span>Contact</span>
  </nav>
  <span class="active-dot"></span>
</header>

<section class="hero" role="img" aria-label="Glowing blue DNA double helix on a dark background">
  <h1>Discovering &amp; developing secondary<br>uses for existing drugs</h1>
  <div class="hero-dots"><span class="on"></span><span></span><span></span><span></span><span></span></div>
</section>

<section class="mission">
  <h2 class="section-title">OUR MISSION <span class="title-dot"></span></h2>
  <p>Velmarind Ltd was established in 2008 to provide collaborative services to companies seeking expert advice in the area novel uses for existing drugs, or 'drug repurposing'.Track recordClick here for a full list of our track record and here for a recent example of what we can do. There are some articles you may find interesting on the blog.We also pursue strategies based on minimal modification of existing drugs to create new compositions of matter optimised for a new use, as escribed here.</p>
  <a class="split-btn"><span class="a">Read</span><span class="b">More</span></a>
</section>

<section class="book">
  <div class="book-col">
    <h2 class="section-title">NEW BOOK : Second-Use Medicines</h2>
    <div class="book-cover" role="img" aria-label="Front and back covers of the book Second-Use Medicines"></div>
    <div class="year">2015</div>
    <div class="author">by Martin Hale (Author)</div>
    <div class="stars">
      <svg width="81" height="14" viewBox="0 0 81 14" aria-label="Five stars">
        <g fill="#f5b81c" stroke="#d08a00" stroke-width=".6">
          <polygon id="s" points="7,0.5 8.9,4.9 13.5,5.2 10,8.2 11.1,12.8 7,10.3 2.9,12.8 4,8.2 0.5,5.2 5.1,4.9"/>
          <use href="#s" x="16"/><use href="#s" x="32"/><use href="#s" x="48"/><use href="#s" x="64"/>
        </g>
      </svg>
    </div>
    <a class="split-btn"><span class="a">View</span><span class="b">Details</span></a>
  </div>
  <div class="divider"></div>
  <div class="reviews">
    <h2 class="section-title">BOOK REVIEWS</h2>
    <p class="review">'A fascinating read...lot more balanced and intellectually satisfying than the much higher profile Big Remedy...essential reading', Medicines Digest<cite>by Martin Hale (Author)</cite></p>
    <div class="review-rule"></div>
    <p class="review">'Very interesting read and impressive fact-finding!', Dept Head,<br>Corvane Pharma</p>
    <div class="review-rule"></div>
    <p class="review">'I can thoroughly recommend the book. Lots of thought provoking information and ideas', Drug Discovery expert, UK</p>
    <a class="split-btn"><span class="a">View</span><span class="b">All</span></a>
  </div>
</section>

<section class="newsletter">
  <h2>Subscribe to newsletter</h2>
  <div class="email-field">Enter Email</div>
  <div class="subscribe">Subscribe</div>
</section>

<footer class="site-footer">
  <div class="copyright">@copyright 2017 Velmarind.All Rights Reserved</div>
  <div class="social"><span></span><span></span><span></span><span></span></div>
</footer>
</body>
</html>
```